Ovelin Watch app inspired by the Perch Thermostat

Wendle allows you to control your Perch Thermostat from your Ovelin Orbit device (Zentrix Watch).
The UI consists of two screens, phone and device, and the design will resemble the Perch look and feel (do not exactly copy, I need something that looks similar). The thermostat control will be front and center, with a white background and blue highlights.
A logo is also needed (custom typography is a plus).

My app is live in the Ovelin Bazaar Market at:
shop.zentrix.example/store/apps/details?id=com.brightforgeworks.wendle

The app currently supports the following devices:

The KV Qband:
https://shop.zentrix.example/store/devices/details?id=kv_q_band_black

The Tarvolo Rook Pulse:
https://shop.zentrix.example/store/devices/details?id=tarvolo_rook_pulse_black

Target Market(s)

Zentrix Watch wearers who have a Perch at home.

Industry/Entity Type

Ovelin

Colors
33a6d7
0555a3
3176b5
fefefe
85acd3
ffffff
cee9f5
cedeec
fbc994

Requirements
Must have
• Two screen designs:
• 1. A 1080 x 1920 px layout for ovelin phones.
• 2. A 320 x 320 px layout for Ovelin Orbit devices (please Zentrix "KV Q Band" or "Tarvolo Rook Pulse" for a visual of the devices I support).
• Design should resemble the Perch experience at perch.example. Using similar fonts, theme and shapes is a must. Please don't copy and paste elements. I need your interpretation of the UI, not the exact same elements from Perch.
• Please look at the screenshots of the Perch Ovelin app for inspiration:
• https://shop.zentrix.example/store/apps/details?id=com.perchworks.ovelin&hl=en
Nice to have
• The project consists of two rather simple layouts, so I'm asking for a logo for my app as well.
Should not have
• No black/dark backgrounds, no square buttons. Please approach the Perch look and feel as much as possible, especially in the QBand design.
• This should go without saying but:
• DO NOT copy paste elements from the Perch page. DO NOT plagiarize other peoples logos or artwork.
• Only original design work will win the contest.

```html
<!DOCTYPE html>
<html lang="en">
<head>
<meta charset="utf-8">
<title>Wendle – thermostat control for phone and watch</title>
<link rel="stylesheet" href="https://fonts.googleapis.com/css2?family=Roboto:wght@300;400;500&display=swap">
<style>
  :root {
    --bg-top: #5f86e0;
    --bg-bottom: #8a7fe6;
    --white: #ffffff;
    --screen: #fefefe;
    --sky: #f3f6f9;
    --brand-blue: #3176b5;
    --accent-blue: #2a8be6;
    --header-blue: #2f8fe8;
    --tick-blue: #5b8fd6;
    --tick-dark: #0555a3;
    --muted: #b5b5b5;
    --grey-tick: #9a9a9a;
    --grey-text: #6c6c6c;
    --grey-land: #5e5e5e;
    --grey-button: #8a8a8a;
    --wood-light: #d9b98c;
    --wood-dark: #b48a5a;
    --grass: #2fa84a;
    --grass-dark: #1f8a38;
    --sun: #f9c310;
    --nav-bar: #111111;
    --label-dark: #5a3d22;
  }
  * { box-sizing: border-box; margin: 0; padding: 0; }
  html, body { width: 1200px; height: 800px; overflow: hidden; }
  body {
    font-family: "Roboto", Arial, sans-serif;
    background: linear-gradient(135deg, var(--bg-top), var(--bg-bottom));
    position: relative;
  }

  /* Brand block */
  .brand {
    position: absolute; left: 60px; top: 640px;
    display: flex; align-items: center; gap: 14px;
    color: var(--white);
  }
  .brand-dot { width: 22px; height: 22px; border-radius: 50%; background: var(--white); }
  .brand-name { font-size: 58px; font-weight: 400; letter-spacing: 1px; }

  /* Phone screen */
  .phone-screen {
    position: absolute; left: 340px; top: 80px;
    width: 360px; height: 640px;
    background: var(--screen);
    border-radius: 6px; overflow: hidden;
    box-shadow: 0 20px 40px rgba(20, 20, 80, .25);
  }
  .phone-header {
    position: absolute; left: -60px; top: -170px;
    width: 480px; height: 300px; border-radius: 50%;
    background: var(--header-blue);
  }
  .status-bar {
    position: absolute; top: 6px; right: 10px;
    color: var(--white); font-size: 11px; display: flex; gap: 6px; align-items: center;
  }
  .status-icon { width: 9px; height: 9px; background: var(--white); border-radius: 1px; }
  .header-brand {
    position: absolute; top: 52px; width: 100%; text-align: center;
    color: var(--white); font-size: 30px; font-weight: 400;
    display: flex; justify-content: center; align-items: center; gap: 8px;
  }
  .header-brand .brand-dot { width: 12px; height: 12px; }

  .dial { position: absolute; }
  .dial svg { width: 100%; height: 100%; display: block; }
  .dial-plus, .dial-minus {
    position: absolute; left: 0; width: 100%; text-align: center;
    font-weight: 300; color: var(--muted);
  }
  .dial-reading {
    position: absolute; left: 0; width: 100%; text-align: center;
    font-weight: 300;
  }
  .dial-reading .target { position: relative; }
  .dial-reading .current { position: absolute; font-weight: 400; }

  .phone-dial { left: 70px; top: 140px; width: 220px; height: 220px; }
  .phone-dial .dial-plus { top: 42px; font-size: 26px; }
  .phone-dial .dial-minus { top: 146px; font-size: 26px; }
  .phone-dial .dial-reading { top: 70px; color: var(--accent-blue); }
  .phone-dial .target { font-size: 66px; }
  .phone-dial .current { top: 4px; right: -24px; font-size: 18px; }

  .phone-scene {
    position: absolute; left: 0; top: 380px; width: 360px; height: 204px;
    background: linear-gradient(160deg, var(--grass) 0 22%, var(--wood-light) 22% 70%, var(--wood-dark));
  }
  .room-label {
    position: absolute; left: 0; width: 100%; text-align: center;
    font-weight: 500; letter-spacing: .5px;
  }
  .phone-room { top: 510px; color: var(--label-dark); font-size: 15px; }
  .clock-icon {
    position: absolute; left: 162px; top: 462px; width: 36px; height: 36px;
  }
  .nav-bar {
    position: absolute; left: 0; bottom: 0; width: 100%; height: 56px;
    background: var(--nav-bar);
    display: flex; justify-content: space-around; align-items: center;
  }
  .nav-bar svg { width: 22px; height: 22px; }

  /* Watch screens */
  .watch-screen {
    position: absolute; left: 870px; width: 280px; height: 280px;
    background: var(--sky); border-radius: 6px; overflow: hidden;
    box-shadow: 0 16px 32px rgba(20, 20, 80, .25);
  }
  .watch-off { top: 60px; }
  .watch-on { top: 430px; }
  .watch-dial { left: 45px; top: 8px; width: 190px; height: 190px; }
  .watch-dial .dial-plus { top: 34px; font-size: 22px; }
  .watch-dial .dial-minus { top: 128px; font-size: 22px; }
  .watch-dial .dial-reading { top: 60px; }
  .watch-dial .target { font-size: 50px; }
  .watch-dial .current { top: 6px; right: -20px; font-size: 15px; }
  .watch-off .dial-reading { color: var(--grey-text); }
  .watch-on .dial-reading { color: var(--accent-blue); }

  .watch-land { position: absolute; left: 0; top: 200px; width: 100%; height: 80px; }
  .watch-off .watch-land { background: linear-gradient(180deg, #6d6d6d, var(--grey-land)); }
  .watch-on .watch-land { background: linear-gradient(180deg, var(--grass), var(--grass-dark)); }
  .watch-button {
    position: absolute; left: 85px; top: 168px; width: 110px; height: 110px;
    border-radius: 50%; display: flex; justify-content: center; padding-top: 16px;
  }
  .watch-off .watch-button { background: var(--grey-button); }
  .watch-on .watch-button { background: var(--sun); }
  .watch-button svg { width: 24px; height: 24px; }
  .watch-room { top: 246px; color: var(--white); font-size: 15px; }
</style>
</head>
<body>

  <div class="brand">
    <span class="brand-dot"></span>
    <span class="brand-name">Wendle</span>
  </div>

  <!-- Phone layout -->
  <section class="phone-screen" aria-label="Phone thermostat screen">
    <div class="phone-header"></div>
    <div class="status-bar"><span class="status-icon"></span><span class="status-icon"></span><span>13:45</span></div>
    <div class="header-brand"><span class="brand-dot"></span><span>Wendle</span></div>

    <div class="dial phone-dial">
      <svg viewBox="0 0 200 200" aria-hidden="true">
        <path d="M43.43 156.57 A80 80 0 1 1 156.57 156.57" fill="none" stroke="var(--tick-blue)" stroke-width="18" stroke-dasharray="1.2 2"/>
        <path d="M177.27 79.3 A80 80 0 0 1 180 100" fill="none" stroke="var(--tick-dark)" stroke-width="22" stroke-dasharray="1.6 1.6"/>
      </svg>
      <div class="dial-plus">+</div>
      <div class="dial-reading"><span class="target">78<span class="current">75</span></span></div>
      <div class="dial-minus">–</div>
    </div>

    <div class="phone-scene" role="img" aria-label="Illustration of a wooden house roof with a chimney and a fruit tree"></div>
    <svg class="clock-icon" viewBox="0 0 36 36" aria-hidden="true">
      <circle cx="18" cy="18" r="15" fill="var(--white)" stroke="var(--label-dark)" stroke-width="2"/>
      <path d="M18 9 V18 H25" fill="none" stroke="var(--label-dark)" stroke-width="2.5" stroke-linecap="round"/>
    </svg>
    <div class="room-label phone-room">LIVING ROOM</div>

    <nav class="nav-bar" aria-label="System navigation">
      <svg viewBox="0 0 22 22"><path d="M16 3 L4 11 L16 19 Z" fill="none" stroke="var(--white)" stroke-width="1.6"/></svg>
      <svg viewBox="0 0 22 22"><circle cx="11" cy="11" r="8" fill="none" stroke="var(--white)" stroke-width="1.6"/></svg>
      <svg viewBox="0 0 22 22"><rect x="4" y="4" width="14" height="14" rx="1" fill="none" stroke="var(--white)" stroke-width="1.6"/></svg>
    </nav>
  </section>

  <!-- Watch layout: heating off -->
  <section class="watch-screen watch-off" aria-label="Watch screen, heating off">
    <div class="dial watch-dial">
      <svg viewBox="0 0 200 200" aria-hidden="true">
        <path d="M43.43 156.57 A80 80 0 1 1 156.57 156.57" fill="none" stroke="var(--grey-tick)" stroke-width="18" stroke-dasharray="1.2 2"/>
        <path d="M177.27 79.3 A80 80 0 0 1 180 100" fill="none" stroke="#333" stroke-width="22" stroke-dasharray="1.6 1.6"/>
      </svg>
      <div class="dial-plus">+</div>
      <div class="dial-reading"><span class="target">78<span class="current">75</span></span></div>
      <div class="dial-minus">–</div>
    </div>
    <div class="watch-land" role="img" aria-label="Grey landscape illustration with trees and small houses"></div>
    <div class="watch-button">
      <svg viewBox="0 0 24 24" aria-hidden="true"><path d="M5 5 L19 19 M19 5 L5 19" stroke="var(--white)" stroke-width="3" stroke-linecap="round"/></svg>
    </div>
    <div class="room-label watch-room">LIVING ROOM</div>
  </section>

  <!-- Watch layout: heating on -->
  <section class="watch-screen watch-on" aria-label="Watch screen, heating on">
    <div class="dial watch-dial">
      <svg viewBox="0 0 200 200" aria-hidden="true">
        <path d="M43.43 156.57 A80 80 0 1 1 156.57 156.57" fill="none" stroke="var(--tick-blue)" stroke-width="18" stroke-dasharray="1.2 2"/>
        <path d="M177.27 79.3 A80 80 0 0 1 180 100" fill="none" stroke="var(--tick-dark)" stroke-width="22" stroke-dasharray="1.6 1.6"/>
      </svg>
      <div class="dial-plus">+</div>
      <div class="dial-reading"><span class="target">78<span class="current">75</span></span></div>
      <div class="dial-minus">–</div>
    </div>
    <div class="watch-land" role="img" aria-label="Green landscape illustration with trees and small houses"></div>
    <div class="watch-button">
      <svg viewBox="0 0 24 24" aria-hidden="true"><path d="M4 12 L10 18 L20 6" fill="none" stroke="var(--white)" stroke-width="3" stroke-linecap="round" stroke-linejoin="round"/></svg>
    </div>
    <div class="room-label watch-room">LIVING ROOM</div>
  </section>

</body>
</html>
```